Business Card Design For A Renovation Contractor Company

We need a business card for a new company based in Singapore, our company name is "KT Planora". We are a renovation contractor that builds designs into reality. We build more of F&B restaurants, retail stores and commercial offices. We work very closely with designers. The final design should communicate to our client that we are a company that you can trust, that will plan and complete your project without giving you a headache. I like my client to remember my company as "KT". The beauty of SIMPLE is important.

Industry/Entity Type

Contractor

Requirements
Nice to have
• Black or Red base

```html
<!DOCTYPE html>
<html lang="en">
<head>
<meta charset="utf-8">
<title>KT Planora – Business Card</title>
<link rel="stylesheet" href="https://fonts.googleapis.com/css2?family=Questrial&display=swap">
<style>
  :root {
    --page-bg: #ece9e6;
    --brand-red: #b3202a;
    --card-black: #0d0d0d;
    --card-white: #ffffff;
    --ink-dark: #2a2a2a;
    --ink-light: #f4f4f4;
  }
  * { margin: 0; padding: 0; box-sizing: border-box; }
  html, body {
    width: 1200px;
    height: 901px;
    overflow: hidden;
    background: var(--page-bg);
  }
  .business-card {
    position: absolute;
    left: 100px;
    top: 165px;
    width: 1000px;
    height: 571px;
    overflow: hidden;
    box-shadow: 0 12px 30px rgba(0,0,0,0.25);
    font-family: "Questrial", sans-serif;
  }
  .card-shapes {
    position: absolute;
    inset: 0;
    width: 100%;
    height: 100%;
  }
  .brand-block {
    position: absolute;
    left: 70px;
    top: 175px;
  }
  .brand-row {
    display: flex;
    align-items: center;
    gap: 16px;
  }
  .brand-dot {
    width: 30px;
    height: 30px;
    border-radius: 50%;
    background: var(--card-black);
  }
  .brand-name {
    font-size: 54px;
    font-weight: 400;
    color: var(--brand-red);
    letter-spacing: -0.5px;
    line-height: 1;
  }
  .brand-tagline {
    margin-top: 8px;
    margin-left: 46px;
    font-size: 19px;
    color: var(--ink-dark);
    letter-spacing: 0.3px;
    white-space: nowrap;
  }
  .contact-details {
    position: absolute;
    left: 585px;
    top: 215px;
    font-size: 22px;
    line-height: 1.45;
    color: var(--ink-light);
    list-style: none;
    white-space: nowrap;
  }
</style>
</head>
<body>
  <article class="business-card">
    <svg class="card-shapes" viewBox="0 0 1000 571" aria-hidden="true">
      <rect width="1000" height="571" fill="var(--brand-red)"/>
      <circle cx="150" cy="110" r="310" fill="var(--card-white)"/>
      <circle cx="930" cy="260" r="410" fill="var(--card-black)" stroke="var(--card-white)" stroke-width="6"/>
    </svg>

    <header class="brand-block">
      <div class="brand-row">
        <span class="brand-dot"></span>
        <h1 class="brand-name">KT Planora</h1>
      </div>
      <p class="brand-tagline">plans made into places, calmly</p>
    </header>

    <ul class="contact-details">
      <li>Email: kelvin@ktplanora.com</li>
      <li>Address: 18 Tanjong Rise road</li>
      <li>#04-2210 Tanjong Rise Complex</li>
      <li>Singapore 438112</li>
    </ul>
  </article>
</body>
</html>
```